HRW / PFB

I need a business card for the owner of sister companies. Please see minimalist version of our old business card for just the Halvorsen business. We need to now have a card that shows off both the Halvorsen logo and the Pale Fern Builders logo. We would like the aesthetic to go well with our brand, and not differ greatly from our Halvorsen cards. These companies are sister companies, there is not one parent company. Looking for a visually appealing design, but not sure if it should be diagonal or something to make it visually attractive... or just some other type of divider. We prefer white logos with a blue background. White transparent background png logos are attached. Please use blue background with hex code 566b7c. The person and contact information will be on the back side, and I can do that myself. We will NOT need to add the text for design-build-sales-installation.

```html
<!DOCTYPE html>
<html lang="en">
<head>
<meta charset="utf-8">
<title>Halvorsen + Pale Fern Builders — Business Card</title>
<link href="https://fonts.googleapis.com/css2?family=Arimo:wght@400;700&family=Montserrat:wght@500;600&display=swap" rel="stylesheet">
<style>
  :root {
    --stage: #1e2023;
    --card-blue: #566b7c;
    --card-blue-deep: #4a5e6f;
    --card-blue-soft: #627a8c;
    --pressed-ink: #3e5162;
    --white: #ffffff;
    --rule: rgba(255,255,255,0.75);
  }
  * { box-sizing: border-box; margin: 0; padding: 0; }
  html, body { width: 1200px; height: 840px; overflow: hidden; }
  body {
    background: var(--stage);
    font-family: "Arimo", Arial, sans-serif;
    position: relative;
  }
  .card {
    position: absolute;
    top: 270px;
    width: 520px;
    height: 300px;
    border-radius: 22px;
    background: var(--card-blue);
    overflow: hidden;
  }
  .card--front { left: 50px; }
  .card--back  { left: 630px; }

  /* Front: Pale Fern Builders */
  .front-brand {
    position: absolute;
    inset: 0;
    display: flex;
    align-items: center;
    justify-content: center;
    gap: 14px;
  }
  .front-brand__mark {
    width: 26px; height: 26px;
    background: var(--pressed-ink);
  }
  .front-brand__name {
    font-family: "Montserrat", Arial, sans-serif;
    font-weight: 600;
    font-size: 30px;
    color: var(--pressed-ink);
    letter-spacing: 0.5px;
  }

  /* Back: Halvorsen contact side */
  .back-wash {
    position: absolute;
    left: 0; top: 70px;
    width: 330px; height: 230px;
    background: linear-gradient(135deg, var(--card-blue-soft) 0%, var(--card-blue-deep) 60%, var(--card-blue) 100%);
    opacity: 0.55;
  }
  .back-brand {
    position: absolute;
    right: 34px; top: 40px;
    display: flex;
    align-items: center;
    gap: 12px;
  }
  .back-brand__mark {
    width: 44px; height: 44px;
    border: 5px solid var(--white);
  }
  .back-brand__name {
    font-family: "Montserrat", Arial, sans-serif;
    font-weight: 600;
    font-size: 28px;
    color: var(--white);
  }
  .back-rule {
    position: absolute;
    left: 170px; right: 30px; top: 120px;
    height: 1px;
    background: var(--rule);
  }
  .address {
    position: absolute;
    right: 34px; top: 140px;
    text-align: right;
    color: var(--white);
    font-size: 13px;
    line-height: 1.35;
  }
  .person {
    position: absolute;
    left: 34px; top: 150px;
    color: var(--white);
  }
  .person__name { font-weight: 700; font-size: 22px; }
  .person__role { font-size: 15px; margin-top: 2px; }
  .person__rule {
    width: 190px; height: 1px;
    background: var(--rule);
    margin: 10px 0 10px;
  }
  .contact { list-style: none; font-size: 14px; line-height: 1.45; }
  .contact li { display: flex; align-items: center; gap: 8px; }
  .contact svg { width: 13px; height: 13px; fill: var(--white); flex: none; }
</style>
</head>
<body>
  <section class="card card--front" aria-label="Card front">
    <div class="front-brand">
      <span class="front-brand__mark"></span>
      <span class="front-brand__name">Pale Fern Builders</span>
    </div>
  </section>

  <section class="card card--back" aria-label="Card back">
    <div class="back-wash" role="img" aria-label="Soft tonal blue wash"></div>
    <div class="back-brand">
      <span class="back-brand__mark"></span>
      <span class="back-brand__name">Halvorsen + Co</span>
    </div>
    <div class="back-rule"></div>
    <p class="address">Your Address, City<br>State, Zip 0000</p>
    <div class="person">
      <p class="person__name">Elliot Marsh</p>
      <p class="person__role">Managing Director</p>
      <div class="person__rule"></div>
      <ul class="contact">
        <li><svg viewBox="0 0 24 24"><path d="M6.6 10.8a15 15 0 0 0 6.6 6.6l2.2-2.2a1 1 0 0 1 1-.25 11.4 11.4 0 0 0 3.6.57 1 1 0 0 1 1 1V20a1 1 0 0 1-1 1A17 17 0 0 1 3 4a1 1 0 0 1 1-1h3.5a1 1 0 0 1 1 1c0 1.25.2 2.45.57 3.6a1 1 0 0 1-.25 1z"/></svg>044-310 552 718</li>
        <li><svg viewBox="0 0 24 24"><path d="M2 5h20v14H2zm2 2v.5l8 5 8-5V7zm0 2.8V17h16V9.8l-8 5z"/></svg>hello@halvorsenco.com</li>
        <li><svg viewBox="0 0 24 24"><circle cx="12" cy="12" r="10"/></svg>www.halvorsenco.com</li>
      </ul>
    </div>
  </section>
</body>
</html>
```